Redesign of a Brochure based on an exsiting example for Web download and email marketing

Can you create a professional brochure based on the attached PDF. We need to keep the name, the logo and the content but everything else can be changed . The PDF will primarily be will be used for web download and email marking but it aslo be printed out for a poster design will be appropriate

Target Market(s)

Business to Business

Industry/Entity Type

Marketing

Font styles to use
Serif

Requirements
Must have
• Must have the existing logo ( in the attached document) and contain the same content

```html
<!DOCTYPE html>
<html lang="en">
<head>
<meta charset="utf-8">
<title>Technology Business Management Framework</title>
<link href="https://fonts.googleapis.com/css2?family=Tinos:wght@400&family=Roboto+Condensed:wght@500&display=swap" rel="stylesheet">
<style>
  :root {
    --stage: #474747;
    --navy: #143a69;
    --box: #4f89c6;
    --white: #ffffff;
    --heading: #1d3f78;
    --ink: #1e1e1e;
    --line: #c9d6e8;
  }
  * { margin: 0; padding: 0; box-sizing: border-box; }
  html, body { width: 1200px; height: 1200px; overflow: hidden; background: var(--stage); }
  .spread {
    position: absolute; left: 50px; top: 200px; width: 1100px; height: 800px;
    display: flex;
  }
  .panel-cover {
    position: relative; width: 549px; height: 100%; background: var(--navy); color: var(--white);
    font-family: "Tinos", "Times New Roman", serif;
  }
  .cover-title { position: absolute; left: 30px; top: 104px; font-size: 46px; font-weight: 400; line-height: 1; }
  .cover-subtitle { position: absolute; left: 30px; top: 170px; font-size: 24px; font-weight: 400; line-height: 28px; }
  .diagram-links { position: absolute; left: 0; top: 0; }
  .node {
    position: absolute; height: 39px; border-radius: 8px; background: var(--box);
    display: flex; align-items: center; justify-content: center;
    font-family: "Roboto Condensed", "Arial Narrow", sans-serif; font-weight: 500; font-size: 16.5px; color: var(--white);
  }
  .node-units { left: 167px; top: 308px; width: 212px; }
  .node-product { left: 29px; top: 393px; width: 212px; }
  .node-service { left: 304px; top: 393px; width: 212px; }
  .node-towers { left: 167px; top: 478px; width: 212px; }
  .node-pools { left: 152px; top: 552px; width: 241px; }
  .node-finance { left: 137px; top: 626px; width: 275px; }

  .panel-article { position: relative; width: 551px; height: 100%; background: var(--white); }
  .article-photo {
    position: absolute; left: 0; top: 0; width: 551px; height: 507px;
    clip-path: polygon(0 0, 100% 0, 100% 507px, 107px 415px, 0 489px);
    background: linear-gradient(160deg, #f4f9fd 0%, #cfe4f4 28%, #6d93bf 55%, #2b4b7c 78%, #162a4c 100%);
  }
  .article-heading {
    position: absolute; left: 30px; top: 487px;
    font-family: "Tinos", "Times New Roman", serif; font-weight: 400; font-size: 18.5px; color: var(--heading);
  }
  .article-body {
    position: absolute; left: 30px; width: 490px;
    font-family: "Tinos", "Times New Roman", serif; font-size: 13px; line-height: 15.6px; color: var(--ink);
    text-align: justify;
  }
  .body-intro { top: 519px; }
  .body-scope { top: 620px; }
  .body-ledger { top: 686px; }
</style>
</head>
<body>
  <main class="spread">
    <section class="panel-cover">
      <h1 class="cover-title">Technology</h1>
      <h2 class="cover-subtitle">Business Management (TBM)<br>Framework</h2>

      <svg class="diagram-links" width="549" height="800" viewBox="0 0 549 800" aria-hidden="true">
        <g stroke="var(--line)" stroke-width="1" fill="none">
          <line x1="135" y1="372" x2="412" y2="372"/>
          <line x1="273" y1="362" x2="273" y2="372"/>
          <line x1="135" y1="452" x2="412" y2="452"/>
          <line x1="273" y1="452" x2="273" y2="462"/>
          <line x1="273" y1="524" x2="273" y2="532"/>
          <line x1="273" y1="598" x2="273" y2="606"/>
        </g>
        <g fill="var(--white)">
          <polygon points="273,356 268,364 278,364"/>
          <polygon points="135,384 130,376 140,376"/>
          <polygon points="412,384 407,376 417,376"/>
          <polygon points="135,437 130,445 140,445"/>
          <polygon points="412,437 407,445 417,445"/>
          <polygon points="273,469 268,461 278,461"/>
          <polygon points="273,503 268,511 278,511"/>
          <polygon points="273,577 268,585 278,585"/>
        </g>
      </svg>

      <div class="node node-units">Business Units</div>
      <div class="node node-product">Product</div>
      <div class="node node-service">Service</div>
      <div class="node node-towers">Technology Towers</div>
      <div class="node node-pools">Cost Pools : Standardised Costs</div>
      <div class="node node-finance">Finance Layer : General Leder Costs</div>
    </section>

    <section class="panel-article">
      <div class="article-photo" role="img" aria-label="Photo of a business team gathered around a laptop in a bright office"></div>
      <h3 class="article-heading">Business Management (TBM) Framework</h3>
      <p class="article-body body-intro">TBM provides a simple but clear way to describe IT costs and how they build into technology towers, services and applications. The next page details the model layers and categories. It splits costs over three broad categories: Build, Manage and Run. In TBM terminology “Run” is IT that supports the existing business while “Build” is equivalent to change the business.</p>
      <p class="article-body body-scope">The TBM model is shown in the diagram opposite. It does not, however, show the projects layer as this is part of the “changethe - business” IT spend and this model focuses mainly on “run-the-business” IT.</p>
      <p class="article-body body-ledger">The cost reference point of the model is the General Ledger, meaning there is always a clear reconciliation with corporate financial systems i.e. A single point of truth.</p>
    </section>
  </main>
</body>
</html>
```